Floor Inspections and Consulting

We provide inspections and consulting services on various floor coverings, e.g. carpet, hardwood, etc. We also do expert witness work for attorneys due to floor covering failures. We current have a logo, just need it incorporated into a new design. I have examples of cards I have found on the internet that capture my attention and make a statement. I have included our original business card, which in my opinion is terrible, but it does have our logo on it.

```html
<!DOCTYPE html>
<html lang="en">
<head>
<meta charset="utf-8">
<title>Keystone Floor Inspections – Business Card</title>
<link href="https://fonts.googleapis.com/css2?family=Open+Sans:wght@300;400;600;700&family=Montserrat:wght@600&display=swap" rel="stylesheet">
<style>
  :root {
    --page: #c9c9c9;
    --paper: #ececec;
    --charcoal: #2d2d2f;
    --gold: #bfa058;
    --gold-deep: #a88a45;
    --ink-soft: #6b6b6b;
    --light-text: #e6e6e6;
  }
  * { margin: 0; padding: 0; box-sizing: border-box; }
  html, body { width: 1200px; height: 1200px; overflow: hidden; }
  body {
    background: var(--page);
    font-family: "Open Sans", Arial, sans-serif;
    position: relative;
  }
  .card {
    position: absolute;
    left: 232px;
    width: 736px;
    height: 422px;
    border-radius: 48px;
    overflow: hidden;
  }
  .card--front { top: 106px; background: var(--charcoal); }
  .card--back { top: 662px; background: var(--charcoal); }

  .front__top {
    position: absolute; left: 0; top: 0; width: 100%; height: 218px;
    background: var(--paper);
    border-bottom: 4px solid var(--gold);
  }
  .brand {
    position: absolute; display: flex; align-items: center; gap: 12px;
  }
  .brand__dot {
    border-radius: 50%; background: var(--gold); flex: none;
  }
  .brand__name {
    font-family: "Open Sans", Arial, sans-serif;
    font-weight: 700; color: var(--gold); letter-spacing: 1px;
  }
  .front .brand { left: 60px; top: 82px; }
  .front .brand__dot { width: 56px; height: 56px; }
  .front .brand__name { font-size: 26px; }

  .tagline {
    position: absolute; right: 82px; top: 78px; text-align: right;
  }
  .tagline__main { font-size: 24px; font-weight: 700; color: var(--gold); line-height: 30px; }
  .tagline__sub { font-size: 20px; font-weight: 400; color: var(--ink-soft); line-height: 26px; }

  .name-tab {
    position: absolute; left: 374px; top: 208px; width: 320px; height: 72px;
    background: var(--gold);
    border: 3px solid var(--paper); border-top: none;
    border-radius: 0 0 14px 14px;
    text-align: center; padding-top: 10px;
  }
  .name-tab__name {
    font-family: "Montserrat", Arial, sans-serif; font-weight: 600;
    font-size: 21px; color: #fff; letter-spacing: 0.5px; line-height: 26px;
  }
  .name-tab__role { font-size: 16px; color: var(--charcoal); line-height: 20px; }

  .address {
    position: absolute; left: 60px; top: 266px;
    color: var(--light-text); font-size: 17px; font-weight: 300; line-height: 21px;
  }
  .contacts {
    position: absolute; left: 60px; top: 331px;
    color: var(--light-text); font-size: 17px; font-weight: 300; line-height: 22px;
    list-style: none;
  }
  .contacts li { display: flex; align-items: center; gap: 10px; }
  .contacts svg { width: 14px; height: 14px; flex: none; }
  .website {
    position: absolute; right: 82px; top: 353px;
    color: var(--light-text); font-size: 17px; font-weight: 300; line-height: 22px;
  }
  .website strong { color: var(--gold); font-weight: 600; }

  .back__glow {
    position: absolute; inset: 0;
    background: radial-gradient(circle at 50% 50%, #4a4436 0%, #3a3732 30%, var(--charcoal) 62%);
  }
  .back .brand {
    left: 50%; top: 50%; transform: translate(-50%, -50%);
  }
  .back .brand__dot { width: 84px; height: 84px; }
  .back .brand__name { font-size: 40px; }
</style>
</head>
<body>

<section class="card card--front front" aria-label="Business card front">
  <div class="front__top">
    <div class="brand">
      <span class="brand__dot"></span>
      <span class="brand__name">KEYSTONE</span>
    </div>
    <div class="tagline">
      <p class="tagline__main">Certified Floor Covering</p>
      <p class="tagline__sub">Inspections &amp; Consulting</p>
    </div>
  </div>

  <div class="name-tab">
    <p class="name-tab__name">MARTIN DELOACHE</p>
    <p class="name-tab__role">President</p>
  </div>

  <p class="address">Keystone Floor Inspections<br>P.O. Box 4417, Ridgefield, CO 80231</p>

  <ul class="contacts">
    <li>
      <svg viewBox="0 0 16 16" aria-hidden="true"><path fill="#bfa058" d="M3.6 1.5l2.3 2.6-1.3 1.8c.9 2 2.5 3.6 4.5 4.5l1.8-1.3 2.6 2.3-1.4 2.4C6.6 13.5 2.5 9.4 1.2 2.9z"/></svg>
      303-555-0148
    </li>
    <li>
      <svg viewBox="0 0 16 16" aria-hidden="true"><rect x="1" y="3.5" width="14" height="9" fill="#bfa058"/><path d="M1 3.5l7 5 7-5" fill="none" stroke="#2d2d2f" stroke-width="1.3"/></svg>
      martin@keystonefloors.com
    </li>
  </ul>

  <p class="website">www.<strong>keystonefloors</strong>.com</p>
</section>

<section class="card card--back back" aria-label="Business card back">
  <div class="back__glow" role="img" aria-label="Soft gold ring pattern radiating from the centre"></div>
  <div class="brand">
    <span class="brand__dot"></span>
    <span class="brand__name">KEYSTONE</span>
  </div>
</section>

</body>
</html>
```